Pim Tavel Brochure Design

We are a Marketing company offering different services. Services must be outlined on design we will provive text for the services once project is accepted.

Service Titles to include in design

Corporate Branding
Marketing
Web Design 
Business Consultation
Printing
Mailing
Automation
Pim Tavel Choice

Please post designs, we have n

Target Market(s)

18+ Years Old

Must have
• Web 2.0 Graphics
• Eye catching design
Nice to have
• Rich Graphics
• Creativity
Should not have
• Standard Templates
• Only bullets

```html
<!DOCTYPE html>
<html lang="en">
<head>
<meta charset="utf-8">
<title>Pim Tavel Marketing – Services Brochure</title>
<link rel="stylesheet" href="https://fonts.googleapis.com/css2?family=Arimo:wght@400;700&display=swap">
<style>
  :root {
    --orange-light: #f9a21f;
    --orange-mid: #f5901f;
    --orange-deep: #ef7d1e;
    --silver: #c6c6c7;
    --white: #ffffff;
    --fold: rgba(255, 255, 255, 0.35);
    --brand-grey: #8f8f91;
  }
  * { margin: 0; padding: 0; box-sizing: border-box; }
  html, body { width: 1200px; height: 848px; overflow: hidden; background: var(--white); }
  .brochure {
    position: relative;
    width: 1200px;
    height: 848px;
    overflow: hidden;
    background: radial-gradient(ellipse at 55% 40%, var(--orange-deep) 0%, var(--orange-mid) 45%, var(--orange-light) 100%);
    font-family: "Arimo", Arial, sans-serif;
    color: var(--white);
  }
  .fold {
    position: absolute;
    top: 0;
    width: 1px;
    height: 100%;
    background: var(--fold);
  }
  .fold--first { left: 394px; }
  .fold--second { left: 788px; }

  .services {
    position: absolute;
    left: 30px;
    top: 27px;
    width: 334px;
  }
  .service { height: 100.6px; }
  .service__title {
    font-size: 19px;
    font-weight: 400;
    line-height: 22px;
  }
  .service__text {
    font-size: 11.7px;
    line-height: 15.2px;
  }

  .globe-art {
    position: absolute;
    left: 790px;
    top: 0;
    width: 410px;
    height: 300px;
    background: radial-gradient(ellipse 60% 80% at 72% 20%, #fbd3a6 0%, #f6b06b 40%, rgba(239, 125, 30, 0) 100%);
  }
  .dot-field {
    position: absolute;
    left: 800px;
    top: 120px;
    width: 400px;
    height: 540px;
    background: radial-gradient(ellipse at 60% 45%, rgba(250, 180, 60, 0.35), rgba(250, 180, 60, 0) 70%);
  }

  .swoosh {
    position: absolute;
    inset: 0;
  }

  .brand {
    position: absolute;
    left: 938px;
    top: 706px;
    display: flex;
    align-items: center;
    gap: 8px;
  }
  .brand__mark {
    width: 16px;
    height: 16px;
    border-radius: 50%;
    background: var(--orange-light);
  }
  .brand__name {
    font-size: 18px;
    font-weight: 700;
    color: var(--brand-grey);
    letter-spacing: 0.5px;
    text-transform: uppercase;
    white-space: nowrap;
  }
</style>
</head>
<body>
<main class="brochure">
  <div class="globe-art" role="img" aria-label="Glossy orange globe built from puzzle pieces"></div>
  <div class="dot-field" role="img" aria-label="Decorative grid of soft orange dots"></div>

  <svg class="swoosh" width="1200" height="848" viewBox="0 0 1200 848" aria-hidden="true">
    <defs>
      <linearGradient id="swoosh-fade" x1="400" y1="0" x2="1200" y2="0" gradientUnits="userSpaceOnUse">
        <stop offset="0" stop-color="#c6c6c7"/>
        <stop offset="0.65" stop-color="#d0d0d1"/>
        <stop offset="1" stop-color="#ffffff"/>
      </linearGradient>
      <linearGradient id="corner-glow" x1="860" y1="848" x2="1200" y2="680" gradientUnits="userSpaceOnUse">
        <stop offset="0" stop-color="#ffffff" stop-opacity="0"/>
        <stop offset="0.5" stop-color="#ffffff" stop-opacity="0.9"/>
        <stop offset="1" stop-color="#ffffff"/>
      </linearGradient>
    </defs>
    <path d="M418,0 C452,290 690,560 1200,590 L1200,622 C670,600 430,310 415,0 Z" fill="url(#swoosh-fade)"/>
    <path d="M424,0 C475,340 700,600 1200,648 L1200,682 C720,700 455,430 419,0 Z" fill="url(#swoosh-fade)"/>
    <path d="M860,848 C950,750 1070,700 1200,682 L1200,848 Z" fill="url(#corner-glow)"/>
  </svg>

  <div class="fold fold--first"></div>
  <div class="fold fold--second"></div>

  <section class="services">
    <article class="service">
      <h2 class="service__title">Corporate Branding</h2>
      <p class="service__text">Lorem ipsum dolor sit amet, consectetuer adipiscing elit. Mauris at leo eu justo tempor pretium. Ut ut arcu eget ipsum consequat interdum. Vivamus nibh purus, ultrices a, fringilla at, pellentesque nec, lacus. Donec sed quam. Quisque accumsan luctus mi.</p>
    </article>
    <article class="service">
      <h2 class="service__title">Marketing</h2>
      <p class="service__text">Lorem ipsum dolor sit amet, consectetuer adipiscing elit. Mauris at leo eu justo tempor pretium. Ut ut arcu eget ipsum consequat interdum. Vivamus nibh purus, ultrices a, fringilla at, pellentesque nec, lacus. Donec sed quam. Quisque accumsan luctus mi.</p>
    </article>
    <article class="service">
      <h2 class="service__title">Web Design</h2>
      <p class="service__text">Lorem ipsum dolor sit amet, consectetuer adipiscing elit. Mauris at leo eu justo tempor pretium. Ut ut arcu eget ipsum consequat interdum. Vivamus nibh purus, ultrices a, fringilla at, pellentesque nec, lacus. Donec sed quam. Quisque accumsan luctus mi.</p>
    </article>
    <article class="service">
      <h2 class="service__title">Business Consultation</h2>
      <p class="service__text">Lorem ipsum dolor sit amet, consectetuer adipiscing elit. Mauris at leo eu justo tempor pretium. Ut ut arcu eget ipsum consequat interdum. Vivamus nibh purus, ultrices a, fringilla at, pellentesque nec, lacus. Donec sed quam. Quisque accumsan luctus mi.</p>
    </article>
    <article class="service">
      <h2 class="service__title">Printing</h2>
      <p class="service__text">Lorem ipsum dolor sit amet, consectetuer adipiscing elit. Mauris at leo eu justo tempor pretium. Ut ut arcu eget ipsum consequat interdum. Vivamus nibh purus, ultrices a, fringilla at, pellentesque nec, lacus. Donec sed quam. Quisque accumsan luctus mi.</p>
    </article>
    <article class="service">
      <h2 class="service__title">Mailing</h2>
      <p class="service__text">Lorem ipsum dolor sit amet, consectetuer adipiscing elit. Mauris at leo eu justo tempor pretium. Ut ut arcu eget ipsum consequat interdum. Vivamus nibh purus, ultrices a, fringilla at, pellentesque nec, lacus. Donec sed quam. Quisque accumsan luctus mi.</p>
    </article>
    <article class="service">
      <h2 class="service__title">Automation</h2>
      <p class="service__text">Lorem ipsum dolor sit amet, consectetuer adipiscing elit. Mauris at leo eu justo tempor pretium. Ut ut arcu eget ipsum consequat interdum. Vivamus nibh purus, ultrices a, fringilla at, pellentesque nec, lacus. Donec sed quam. Quisque accumsan luctus mi.</p>
    </article>
    <article class="service">
      <h2 class="service__title">Pim Tavel Choice</h2>
      <p class="service__text">Lorem ipsum dolor sit amet, consectetuer adipiscing elit. Mauris at leo eu justo tempor pretium. Ut ut arcu eget ipsum consequat interdum. Quisque accumsan luctus mi.</p>
    </article>
  </section>

  <div class="brand">
    <span class="brand__mark"></span>
    <span class="brand__name">Pim Tavel Marketing</span>
  </div>
</main>
</body>
</html>
```